Business Card for boutique psychology business

Business card for boutique psychology practice in Melbourne. I want them to be relatively simply with the logo and backing colour taking up the front side. Then, text on the back, with my name; professional title (Clinical Psychologist); website - torvinpsychology.com.au; email: hello@torvinpsychology.com.au; insta: @torvin.psychology.emdr
Back should also have the words: Connect. Integrate. Evolve
Fonts used for logo are: Mikea Demo and Gotham Medium. Use something for back text that will compliment these.
Brand colours uploaded below. I'd like to see options in both olive and blush.

```html
<!DOCTYPE html>
<html lang="en">
<head>
<meta charset="utf-8">
<title>Torvin Psychology + EMDR — Business Card</title>
<link href="https://fonts.googleapis.com/css2?family=Montserrat:wght@300;400;500&family=Josefin+Sans:wght@300&display=swap" rel="stylesheet">
<style>
  :root {
    --backdrop: #2b2b2b;
    --olive: #434530;
    --blush: #ecc9b4;
    --card-shadow: rgba(0, 0, 0, 0.45);
  }
  * { margin: 0; padding: 0; box-sizing: border-box; }
  html, body {
    width: 1200px;
    height: 689px;
    overflow: hidden;
    background: var(--backdrop);
  }
  .sheet {
    position: relative;
    width: 1200px;
    height: 689px;
    display: flex;
    align-items: center;
    justify-content: center;
    gap: 40px;
  }
  .card {
    position: relative;
    width: 530px;
    height: 308px;
    background: var(--olive);
    border-radius: 18px;
    box-shadow: 0 14px 34px var(--card-shadow);
    color: var(--blush);
  }

  /* Front */
  .card-front {
    display: flex;
    flex-direction: column;
    align-items: center;
    justify-content: center;
  }
  .brand-name {
    font-family: "Montserrat", sans-serif;
    font-weight: 500;
    font-size: 78px;
    line-height: 1;
    letter-spacing: 1px;
  }
  .brand-descriptor {
    font-family: "Montserrat", sans-serif;
    font-weight: 500;
    font-size: 21px;
    letter-spacing: 1px;
    margin-top: 6px;
  }
  .tagline {
    font-family: "Montserrat", sans-serif;
    font-weight: 400;
    font-size: 11px;
    letter-spacing: 1.2px;
    margin-top: 34px;
  }

  /* Back */
  .card-back {
    display: flex;
    align-items: center;
    padding: 0 40px 0 70px;
  }
  .identity {
    text-align: left;
    width: 170px;
  }
  .person-name {
    font-family: "Josefin Sans", sans-serif;
    font-weight: 300;
    font-size: 24px;
    letter-spacing: 2px;
    text-transform: uppercase;
    white-space: nowrap;
  }
  .person-title {
    font-family: "Montserrat", sans-serif;
    font-weight: 400;
    font-size: 11.5px;
    letter-spacing: 0.6px;
    margin-top: 4px;
  }
  .divider {
    width: 1px;
    height: 112px;
    background: var(--blush);
    margin: 0 22px 0 24px;
  }
  .contact-list {
    list-style: none;
    font-family: "Montserrat", sans-serif;
    font-weight: 400;
    font-size: 11px;
    letter-spacing: 0.4px;
  }
  .contact-item {
    display: flex;
    align-items: center;
    gap: 8px;
    line-height: 1;
    margin: 7px 0;
    white-space: nowrap;
  }
  .contact-icon {
    width: 11px;
    height: 11px;
    flex: none;
  }
</style>
</head>
<body>
<main class="sheet">

  <section class="card card-front" aria-label="Card front">
    <div class="brand-name">torvin</div>
    <div class="brand-descriptor">psychology + EMDR</div>
    <div class="tagline">Connect. Integrate. Evolve</div>
  </section>

  <section class="card card-back" aria-label="Card back">
    <div class="identity">
      <div class="person-name">Liam Carter</div>
      <div class="person-title">Clinical Psychologist</div>
    </div>
    <div class="divider"></div>
    <ul class="contact-list">
      <li class="contact-item">
        <svg class="contact-icon" viewBox="0 0 12 12" aria-hidden="true">
          <path d="M2.5 1h2l1 2.6-1.3.9a6 6 0 0 0 3.3 3.3l.9-1.3L11 7.5v2A1.5 1.5 0 0 1 9.5 11 8.5 8.5 0 0 1 1 2.5 1.5 1.5 0 0 1 2.5 1z" fill="var(--blush)"/>
        </svg>
        <span>(03) 5550 1427</span>
      </li>
      <li class="contact-item">
        <svg class="contact-icon" viewBox="0 0 12 12" aria-hidden="true">
          <rect x="0.5" y="2.5" width="11" height="7.5" rx="0.8" fill="var(--blush)"/>
          <path d="M1 3l5 3.6L11 3" fill="none" stroke="var(--olive)" stroke-width="1"/>
        </svg>
        <span>hello@torvinpsychology.com.au</span>
      </li>
      <li class="contact-item">
        <svg class="contact-icon" viewBox="0 0 12 12" aria-hidden="true">
          <circle cx="6" cy="6" r="5" fill="none" stroke="var(--blush)" stroke-width="1.1"/>
          <ellipse cx="6" cy="6" rx="2.2" ry="5" fill="none" stroke="var(--blush)" stroke-width="0.9"/>
          <path d="M1 6h10" stroke="var(--blush)" stroke-width="0.9"/>
        </svg>
        <span>www.torvinpsychology.com.au</span>
      </li>
      <li class="contact-item">
        <svg class="contact-icon" viewBox="0 0 12 12" aria-hidden="true">
          <circle cx="6" cy="6" r="4.5" fill="none" stroke="var(--blush)" stroke-width="1.2"/>
        </svg>
        <span>@torvin.psychology.emdr</span>
      </li>
    </ul>
  </section>

</main>
</body>
</html>
```